Not another boring Business Card Design Project

This is not another boring Business Card Design Project.

We are looking for the weirdest, wackiest most boundary pushing designs that you can come up with.

If you believe that design can be fun, energetic, crazy, unpredictable, beautiful and eye-catching then read on… this project is for you.

We are Tolvin Presk and we print plastic cards.

We are running a Plastic Card Design Competition.

And we need a plastic card to advertise the competition to graphic designers just like you.

The design needs to make your average designers’ jaws drop and their eyes pop out.

You can do what you wish with the card design, so long as it stands out.

We like these designs, designs that stretch the boundaries and become something beyond just another business card:

http://quorvamedia.net/wp-content/uploads/2009/03/b48.jpg
Designer - http://www.pelvanworks.com/

http://quorvamedia.net/wp-content/uploads/2009/03/b41.jpg
Designer - http://renolbrakstad.com/

http://images.plinthhive.com/designs/44195_732292_37774_thumbnail.jpg
Designer- Zentro Media at Plinth Hive

http://images.plinthhive.com/designs/44195_717529_37774_thumbnail.jpg
Designer - Zentro Media at Plinth Hive

http://quorvamedia.net/wp-content/uploads/2009/03/b11.jpg
Designer - http://www.wk7studio.com/

http://quorvamedia.net/wp-content/uploads/2009/03/b16.jpg
Designer - http://www.pebbletumbler.com/

Reason: A number of designers have said they want to submit designs and haven't yet done so, we want to give them time.

Reason: We've extended the deadline by 4 days for those who want to submit their designs over the weekend and give ourselves time to judge them

Plastic

• The design needs to contain this link: lnk.example/QzRpLk and any other detail that will encourage competition entry. The design will be printed on plastic.
• No borders (when plastic cards are punched to shape and size there is movement of 1 - 2mm, borders highlight this movement).

Keep text 3mm away from edges of the cards.

Please don't create designs to be produced on clear/transparent plastic.

```html
<!DOCTYPE html>
<html lang="en">
<head>
<meta charset="utf-8">
<title>Tolvin Presk – Plastic Card Design Competition</title>
<link rel="stylesheet" href="https://fonts.googleapis.com/css2?family=Open+Sans:wght@300;400;600&family=Allura&display=swap">
<style>
  :root {
    --backdrop: #dcd9d6;
    --card-white: #ffffff;
    --card-black: #050505;
    --ink: #111111;
    --ink-soft: #333333;
    --gold-light: #d9cfa6;
    --gold: #b9ab7c;
    --gold-deep: #5e5640;
    --plum-ink: #1f1624;
    --plum-mid: #4a3f50;
  }
  * { box-sizing: border-box; margin: 0; padding: 0; }
  html, body {
    width: 1200px;
    height: 1106px;
    overflow: hidden;
    background: var(--backdrop);
  }
  .stage { position: relative; width: 1200px; height: 1106px; }

  .card {
    position: absolute;
    top: 143px;
    width: 500px;
    height: 820px;
    overflow: hidden;
  }

  /* Designer identity card */
  .card--designer { left: 70px; background: var(--card-white); }
  .card--designer .artwork {
    position: absolute; left: 0; top: 0; width: 500px; height: 600px;
    background:
      radial-gradient(ellipse 120px 200px at 18% 28%, rgba(31,22,36,.85) 0%, rgba(31,22,36,0) 100%),
      radial-gradient(ellipse 160px 130px at 62% 34%, rgba(31,22,36,.9) 0%, rgba(31,22,36,0) 100%),
      radial-gradient(ellipse 140px 190px at 40% 72%, rgba(31,22,36,.9) 0%, rgba(31,22,36,0) 100%),
      radial-gradient(ellipse 110px 120px at 80% 64%, rgba(74,63,80,.8) 0%, rgba(74,63,80,0) 100%),
      radial-gradient(ellipse 260px 300px at 45% 45%, rgba(74,63,80,.55) 0%, rgba(255,255,255,0) 100%),
      var(--card-white);
  }
  .studio-name {
    position: absolute; left: 30px; top: 640px;
    font-family: "Open Sans", sans-serif; font-weight: 300;
    font-size: 40px; line-height: 1; color: var(--ink);
    letter-spacing: -1px;
  }
  .discipline {
    position: absolute; left: 30px; top: 700px;
    font-family: "Open Sans", sans-serif; font-weight: 600;
    font-size: 12.5px; color: var(--ink); letter-spacing: -0.2px;
  }
  .designer-name {
    position: absolute; left: 232px; top: 612px;
    font-family: "Allura", cursive; font-size: 38px; color: var(--ink);
  }
  .contact-list {
    position: absolute; left: 232px; top: 668px; list-style: none;
    font-family: "Open Sans", sans-serif; font-size: 14px; color: var(--ink-soft);
  }
  .contact-list li { display: flex; align-items: center; gap: 10px; height: 20px; }
  .contact-list svg { width: 11px; height: 11px; flex: none; }

  /* Competition card */
  .card--competition { left: 630px; background: var(--card-black); }
  .card--competition .artwork {
    position: absolute; left: 0; top: 0; width: 500px; height: 660px;
    background:
      radial-gradient(ellipse 140px 110px at 28% 22%, rgba(217,207,166,.85) 0%, rgba(217,207,166,0) 100%),
      radial-gradient(ellipse 170px 150px at 62% 40%, rgba(185,171,124,.9) 0%, rgba(185,171,124,0) 100%),
      radial-gradient(ellipse 130px 180px at 30% 70%, rgba(185,171,124,.85) 0%, rgba(185,171,124,0) 100%),
      radial-gradient(ellipse 150px 120px at 78% 76%, rgba(217,207,166,.7) 0%, rgba(217,207,166,0) 100%),
      radial-gradient(ellipse 280px 330px at 50% 50%, rgba(94,86,64,.8) 0%, rgba(5,5,5,0) 100%),
      var(--card-black);
  }
  .info-band {
    position: absolute; left: 0; top: 660px; width: 500px; height: 160px;
    background: var(--card-white);
  }
  .client-name {
    position: absolute; left: 30px; top: 42px;
    font-family: "Open Sans", sans-serif; font-weight: 400;
    font-size: 36px; line-height: 1; color: var(--ink); letter-spacing: -1.5px;
  }
  .tagline {
    position: absolute; left: 32px; top: 92px;
    font-family: "Open Sans", sans-serif; font-weight: 400;
    font-size: 11px; letter-spacing: 0.42em; color: var(--ink);
  }
  .band-divider {
    position: absolute; left: 272px; top: 38px; width: 1.5px; height: 68px;
    background: var(--ink);
  }
  .entry-link {
    position: absolute; left: 288px; top: 62px;
    font-family: "Open Sans", sans-serif; font-weight: 400;
    font-size: 12.5px; color: var(--ink);
  }
</style>
</head>
<body>
<main class="stage">

  <section class="card card--designer">
    <div class="artwork" role="img" aria-label="Flowing black ink illustration of swirling ribbons and petal forms"></div>
    <div class="studio-name">Voss Studio</div>
    <div class="discipline">illustrationgraphicdesign</div>
    <div class="designer-name">Mirela Voss</div>
    <ul class="contact-list">
      <li>
        <svg viewBox="0 0 12 12"><circle cx="6" cy="6" r="6" fill="#333"/><path d="M4 3.2h1.3l.5 1.5-.8.6a4 4 0 0 0 1.7 1.7l.6-.8 1.5.5v1.3C7 8.3 3.7 5 4 3.2z" fill="#fff"/></svg>
        +65 9120 4471
      </li>
      <li>
        <svg viewBox="0 0 12 12"><circle cx="6" cy="6" r="6" fill="#333"/><rect x="3" y="4" width="6" height="4.2" fill="none" stroke="#fff" stroke-width=".9"/><path d="M3 4l3 2.3L9 4" fill="none" stroke="#fff" stroke-width=".9"/></svg>
        mira.inks@postmail.net
      </li>
      <li>
        <svg viewBox="0 0 12 12"><circle cx="6" cy="6" r="6" fill="#333"/><circle cx="6" cy="6" r="3" fill="none" stroke="#fff" stroke-width=".8"/><path d="M3 6h6M6 3c-1.4 1.6-1.4 4.4 0 6M6 3c1.4 1.6 1.4 4.4 0 6" fill="none" stroke="#fff" stroke-width=".7"/></svg>
        mirainks.folioworks.com
      </li>
    </ul>
  </section>

  <section class="card card--competition">
    <div class="artwork" role="img" aria-label="Gold line illustration of swirling ribbons and petal forms on black"></div>
    <div class="info-band">
      <div class="client-name">Tolvin Presk</div>
      <div class="tagline">design.win.exposure</div>
      <div class="band-divider"></div>
      <div class="entry-link">visit : lnk.example/QzRpLk</div>
    </div>
  </section>

</main>
</body>
</html>
```